■レイアウトの希望について
◎全体の左右のサイズは、1000px~1100pxくらいでお願いします。
※左右のサイドにナビを入れる場合は、左右300pxでお願いします。
◎現在のレイアウトは無視してください。
◎重要箇所を目立たせて、全体的にバランスよく配置させてください。
※重要箇所の順位は以下の通りです。
(1)検索ページへの入り口ブロック
(2)記事ページへのナビゲーション
(3)「イチオシ学生会館紹介サイト」と「オススメ学生会館」
(4)「学生会館以外のお部屋探し」
(5)「TOPICS」と「オススメ情報」
※見本のPDFは左ナビがあるようにレイアウトしていますが、トップページは2カラムにせず、1カラムでもかまいません。
(トップページに入れたいブロックを記載しただけですのでレイアウトの希望ではありません)
ただし、サブページは左右どちらかにナビを置く形の2カラムでお願いします。
(サブページのナビに入れるのは、記事ページへのナビゲーションと「学生会館以外のお部屋探し」のみです)

■デザインの希望について
◎落ち着いた感じのバランスの良いデザイン案が希望です。
※色数を多く使ったごちゃごちゃした配置は好みではありません。
※色は派手な感じでなく落ち着いた色が希望ですが、くすんだ色は好みではありません。
◎以前にタスクモアで依頼して作成した下記サイトもご参照ください。
http://www.sorahane-dorm.net/
http://www.qz7.net/
http://www.finerm.com/
http://222.xuu.jp/tomoya.net/
※一番下のみ現在作成中のため仮URLです。(全ページは完成していません)

■その他の希望について
◎ヘッダーはスマホサイズになった場合のことも考えて作成してください。
◎提案内で使用するイメージ画像は無料の素材サイトか、有料画像を使用する場合は、FOLMIOをご利用ください。
https://folmio-img.jp/
※現在サイト内にある画像を使用いただく形でもかまいません。

なお、初回のご提案はできるだけ締切日の2日前までにお願いします。
ギリギリの場合は修正依頼が間に合わず、候補になる良いご提案でも見送る場合がありますので..。

以上になりますので、ご提案のほど、よろしくお願いいたします。
http://www.heyanavi-dorm.net/
3ページ
基本的にはお任せですが、派手な色やくすんだ色は避けてください。(バランスの良い、落ち着いた色が希望)
• 高解像度JPG (.jpg)
• フォトショップ形式 (.psd)
JPG・PNGはどちらでもかまいません。
残り2日になりましたが、提案がないので締切日を延長いたします。

依頼詳細にも記載しましたが、できるだけ締切日の2日前までに初回のご提案をお送りいただけましたら幸いです。

その他、ご要望などがございましたら、メッセージからお送りください。
ロゴは現在のものは使用せず、見本と同様の一般的な横長のものを希望します。
(ロゴではなくて書体をそのまま使用する形でもかまいません)
弊社希望の「全体の左右のサイズは、1000px~1100pxくらい」とうのは、実際に文章や画像が入る本文(左右ナビが入る場合はその外側まで)のサイズになりますので、ご確認ください。

なお、すでにご提案を作成中の場合で、上記に当てはまらない場合はそのまま進めていただいてもかまいません。

とりあえず、デザインが分かれば問題ありませんので..。

※実際にお仕事を依頼することになった場合は、修正をお願いします。
お仕事が決まったあとに作成していただく、サブページのレイアウトを作成しましたので添付します。

決定したトップページと同じ方向性で、こちらのサブページも作成いただく形でお願いします。
今月末まで多忙になり、選考作業や細かい修正依頼作業がすぐにはできそうもないので、締切日をギリギリまで延ばさせていただきます。

必ず当選者は選定させていただきますので、よろしくお願いいたします。

また、依頼金額も若干アップさせていただきました。

全体的なバランスが良く、ごちゃごちゃしていなくて、統一感があり落ち着いた感じのご提案でした。

ご提案をいただき、ありがとうございました。
部分的には気に入ったご提案もあったのですが、全体的なバランスやメリハリといった点で、採用した案を選びました。
申し訳ございませんがご了承ください。
なお、今後も複数サイトのリニューアル依頼をタスクモアに出しますので、機会がございましたら、よろしくお願いいたします。

```html
<!DOCTYPE html>
<html lang="ja">
<head>
<meta charset="utf-8">
<title>キャンパス寮ナビ</title>
<link rel="stylesheet" href="https://fonts.googleapis.com/css2?family=M+PLUS+Rounded+1c:wght@500;700;800&family=Noto+Sans+JP:wght@400;500;700&display=swap">
<style>
:root{
  --green:#8cc63f;
  --green-dark:#6fa82a;
  --green-pale:#eef7e2;
  --teal:#34a7c2;
  --teal-dark:#2a8fa8;
  --orange:#f39a2b;
  --ink:#444;
  --ink-soft:#777;
  --line:#dcdcdc;
  --about-bg:#e8eef2;
  --footer:#3d3d3d;
  --white:#fff;
}
*{box-sizing:border-box;margin:0;padding:0}
html,body{width:1200px;height:2712px;overflow:hidden}
body{font-family:"Noto Sans JP",sans-serif;color:var(--ink);background:var(--white);font-size:12px;line-height:1.5}
ul{list-style:none}
.wrap{width:760px;margin:0 auto;position:relative}

/* header */
.site-header{height:60px;text-align:center;background:var(--white)}
.site-header .tagline{font-size:10px;color:var(--ink-soft);padding-top:4px;height:18px}
.logo{display:inline-flex;align-items:center;gap:6px;font-family:"M PLUS Rounded 1c",sans-serif;font-weight:800;font-size:22px;color:var(--teal-dark);margin-top:4px}
.logo .dot{width:14px;height:14px;border-radius:50%;background:var(--orange)}

/* hero */
.hero{height:380px;position:relative}
.hero-photo{position:absolute;inset:0;background:linear-gradient(100deg,#d9dcd8 0%,#f1efe9 35%,#f7f5f0 60%,#e9ece6 100%)}
.hero-copy{position:absolute;left:520px;top:160px;background:var(--green);color:var(--white);font-family:"M PLUS Rounded 1c",sans-serif;font-weight:700;font-size:19px;padding:8px 18px;border-radius:3px}

/* search */
.search{height:280px;padding-top:30px}
.search-panel{background:var(--green);border-radius:4px;padding:22px 26px;height:230px}
.search-row{display:flex;background:var(--white);border-radius:3px;height:40px;overflow:hidden}
.search-label{background:var(--teal);color:var(--white);font-weight:700;font-size:13px;width:130px;display:flex;align-items:center;justify-content:center}
.search-input{flex:1;display:flex;align-items:center;padding-left:14px;color:#aaa;font-size:12px}
.search-btn{width:90px;background:var(--orange);color:var(--white);font-weight:700;display:flex;align-items:center;justify-content:center;font-size:14px}
.search-note{color:var(--white);font-size:10.5px;margin:10px 0 14px;line-height:1.6}
.search-ways{display:flex;gap:14px}
.search-way{flex:0 0 150px;height:70px;background:var(--white);border-radius:4px;display:flex;align-items:center;gap:10px;padding-left:18px;font-weight:700;color:var(--green-dark);font-size:13px}
.search-way .ic{width:38px;height:38px;border-radius:50%;background:var(--green);display:flex;align-items:center;justify-content:center}

.skyline{height:40px;background:linear-gradient(var(--white),#eef2f4)}

/* section headings */
.sec-title{text-align:center;font-family:"M PLUS Rounded 1c",sans-serif;font-weight:700;font-size:22px;color:var(--ink);padding:34px 0 24px}
.sec-title::after{content:"";display:block;width:40px;height:3px;background:var(--green);margin:8px auto 0}

/* about */
.about{height:450px;background:var(--about-bg)}
.about-grid{display:grid;grid-template-columns:repeat(5,1fr);gap:12px}
.about-tile{height:120px;background:var(--teal);color:var(--white);border-radius:3px;display:flex;flex-direction:column;align-items:center;justify-content:center;gap:10px;font-size:11.5px;font-weight:700;text-align:center;line-height:1.35}

/* picks */
.picks{height:400px;position:relative}
.picks-bg{position:absolute;inset:0;background:linear-gradient(90deg,#cfd8dc,#e6ebe7 50%,#d6dde0)}
.picks .wrap{display:flex;gap:30px;padding-top:30px}
.pick-box{flex:1;background:rgba(255,255,255,.95);border-radius:4px;padding:0 18px 18px;height:330px}
.pick-box h2{font-family:"M PLUS Rounded 1c",sans-serif;font-weight:700;font-size:18px;text-align:center;padding:18px 0 12px;border-bottom:2px solid var(--green);margin-bottom:8px}
.pick-box li{font-size:12px;padding:9px 0 9px 16px;border-bottom:1px dotted var(--line);position:relative}
.pick-box li::before{content:"";position:absolute;left:2px;top:14px;border:4px solid transparent;border-left-color:var(--green)}
.pick-box li em{font-style:normal;color:var(--teal-dark);font-weight:700}

/* rooms */
.rooms{height:290px}
.rooms .sec-title{padding-top:26px;padding-bottom:18px}
.room-grid{display:grid;grid-template-columns:repeat(3,1fr);gap:10px 20px}
.room-card{display:flex;align-items:center;gap:10px;border:1px solid var(--line);height:46px;padding-right:8px}
.room-img{width:70px;height:44px;background:linear-gradient(135deg,#d7e4ea,#f1ece2)}
.room-card span{font-size:11.5px;font-weight:700;color:var(--teal-dark);line-height:1.3}

/* topics */
.news{height:590px}
.news .wrap{display:flex;gap:40px}
.news-col{flex:1}
.news-col h2{font-family:"M PLUS Rounded 1c",sans-serif;font-weight:700;font-size:20px;text-align:center;padding:30px 0 16px}
.news-col h2::after{content:"";display:block;width:40px;height:3px;background:var(--green);margin:6px auto 0}
.news-col li{font-size:11.5px;padding:10px 4px;border-bottom:1px solid var(--line);line-height:1.45}
.news-col li::before{content:"›";color:var(--green);font-weight:700;margin-right:6px}
.page-top{position:absolute;right:0;top:548px;width:30px;height:30px;background:var(--green);border-radius:3px;display:flex;align-items:center;justify-content:center}

/* footer */
.site-footer{height:232px;background:var(--footer);color:#ccc;text-align:center;padding-top:40px;font-size:11px}
.site-footer nav{margin-bottom:12px}
.site-footer nav a{color:#ddd;text-decoration:none;margin:0 8px}
</style>
</head>
<body>

<header class="site-header">
  <p class="tagline">一人暮らし学生の部屋探しをサポートする「学生会館」情報サイト</p>
  <div class="logo"><span class="dot"></span>キャンパス寮ナビ</div>
</header>

<section class="hero">
  <div class="hero-photo" role="img" aria-label="寮の談話室でくつろぐ学生たちの写真"></div>
  <p class="hero-copy">学生のための安心で快適な学生会館情報満載</p>
</section>

<section class="search">
  <div class="wrap search-panel">
    <div class="search-row">
      <div class="search-label">学生会館を探す</div>
      <div class="search-input">学校名や駅名・キーワードを入力</div>
      <div class="search-btn">検索</div>
    </div>
    <p class="search-note">※ 学校名・駅名・地域名などから全国の学生会館を検索できます。<br>※ 食事付き・女子専用などの条件でも絞り込みができます。</p>
    <div class="search-ways">
      <div class="search-way"><span class="ic"><svg width="20" height="20" viewBox="0 0 20 20"><path d="M10 2a6 6 0 0 0-6 6c0 4.5 6 10 6 10s6-5.5 6-10a6 6 0 0 0-6-6z" fill="#fff"/><circle cx="10" cy="8" r="2.2" fill="#8cc63f"/></svg></span>地域から探す</div>
      <div class="search-way"><span class="ic"><svg width="20" height="20" viewBox="0 0 20 20"><rect x="5" y="3" width="10" height="11" rx="2" fill="#fff"/><path d="M6 17l2-3M14 17l-2-3" stroke="#fff" stroke-width="1.6"/><rect x="7" y="5" width="6" height="4" fill="#8cc63f"/></svg></span>沿線から探す</div>
      <div class="search-way"><span class="ic"><svg width="20" height="20" viewBox="0 0 20 20"><path d="M6 3v14M4 3v4a2 2 0 0 0 4 0V3M14 3c-2 0-2 6 0 7v7" stroke="#fff" stroke-width="1.6" fill="none"/></svg></span>条件から探す</div>
    </div>
  </div>
</section>

<div class="skyline"></div>

<section class="about">
  <div class="wrap">
    <h2 class="sec-title">学生会館について</h2>
    <ul class="about-grid">
      <li class="about-tile"><svg width="30" height="30" viewBox="0 0 30 30"><path d="M5 14L15 5l10 9v11H5z" fill="none" stroke="#fff" stroke-width="2"/></svg>学生会館って<br>どんなところ？</li>
      <li class="about-tile"><svg width="30" height="30" viewBox="0 0 30 30"><path d="M15 4v22M8 10h14M8 18h14" stroke="#fff" stroke-width="2"/></svg>学生会館入居への<br>流れ</li>
      <li class="about-tile"><svg width="30" height="30" viewBox="0 0 30 30"><path d="M15 4v22M6 9h18M6 9l-3 8h6zM24 9l-3 8h6z" stroke="#fff" stroke-width="2" fill="none"/></svg>学生会館 VS<br>アパート徹底比較</li>
      <li class="about-tile"><svg width="30" height="30" viewBox="0 0 30 30"><rect x="7" y="4" width="16" height="22" fill="none" stroke="#fff" stroke-width="2"/><path d="M11 11h8M11 16h8M11 21h5" stroke="#fff" stroke-width="2"/></svg>寮・学生会館<br>レポート</li>
      <li class="about-tile"><svg width="30" height="30" viewBox="0 0 30 30"><circle cx="13" cy="13" r="7" fill="none" stroke="#fff" stroke-width="2"/><path d="M18 18l7 7" stroke="#fff" stroke-width="2"/></svg>学生会館の<br>選び方</li>
      <li class="about-tile"><svg width="30" height="30" viewBox="0 0 30 30"><circle cx="11" cy="13" r="7" fill="none" stroke="#fff" stroke-width="2"/><circle cx="20" cy="17" r="7" fill="none" stroke="#fff" stroke-width="2"/></svg>学生会館<br>Q&amp;A</li>
      <li class="about-tile"><svg width="30" height="30" viewBox="0 0 30 30"><path d="M5 12h6l10-6v18l-10-6H5z" fill="none" stroke="#fff" stroke-width="2"/></svg>生活の知恵</li>
      <li class="about-tile"><svg width="30" height="30" viewBox="0 0 30 30"><circle cx="15" cy="15" r="10" fill="none" stroke="#fff" stroke-width="2"/><path d="M15 9v6l4 3" stroke="#fff" stroke-width="2" fill="none"/></svg>学生会館の<br>一日</li>
      <li class="about-tile"><svg width="30" height="30" viewBox="0 0 30 30"><rect x="5" y="6" width="20" height="18" fill="none" stroke="#fff" stroke-width="2"/><path d="M5 11h20" stroke="#fff" stroke-width="2"/></svg>入居時期と<br>スケジュール</li>
      <li class="about-tile"><svg width="30" height="30" viewBox="0 0 30 30"><circle cx="15" cy="15" r="10" fill="none" stroke="#fff" stroke-width="2"/><path d="M12 12a3 3 0 1 1 3 3v3M15 21v1" stroke="#fff" stroke-width="2" fill="none"/></svg>よくある<br>質問</li>
    </ul>
  </div>
</section>

<section class="picks">
  <div class="picks-bg" role="img" aria-label="明るい学生寮の室内写真（ぼかし）"></div>
  <div class="wrap">
    <div class="pick-box">
      <h2>イチオシ学生会館紹介サイト</h2>
      <ul>
        <li><em>学生会館なら</em> 首都圏の空室情報サイト</li>
        <li>関西圏の学生会館 <em>ガイド</em></li>
        <li>女子学生専用マンション <em>特集サイト</em></li>
        <li>食事付き学生会館の専門情報</li>
        <li>新入生向け <em>部屋探しナビ</em></li>
      </ul>
    </div>
    <div class="pick-box">
      <h2>オススメ学生会館</h2>
      <ul>
        <li>駅から徒歩3分の <em>学生会館</em> 都心エリア</li>
        <li>朝夕2食付き・管理人常駐の安心 <em>学生会館</em></li>
        <li>新築・オートロック完備の女子専用館</li>
        <li>大学キャンパスまで自転車5分の館</li>
      </ul>
    </div>
  </div>
</section>

<section class="rooms">
  <div class="wrap">
    <h2 class="sec-title">学生会館以外のお部屋探し</h2>
    <ul class="room-grid">
      <li class="room-card"><div class="room-img" role="img" aria-label="マンションの外観写真"></div><span>学生マンション<br>一覧情報</span></li>
      <li class="room-card"><div class="room-img" role="img" aria-label="学生寮の個室写真"></div><span>一人暮らし向け<br>賃貸物件ガイド</span></li>
      <li class="room-card"><div class="room-img" role="img" aria-label="ルームシェアの共有スペース写真"></div><span>ルームシェア<br>物件特集</span></li>
      <li class="room-card"><div class="room-img" role="img" aria-label="女子学生の部屋写真"></div><span>女子学生専用<br>マンション</span></li>
      <li class="room-card"><div class="room-img" role="img" aria-label="下宿の和室写真"></div><span>下宿・ホームステイ<br>情報</span></li>
      <li class="room-card"><div class="room-img" role="img" aria-label="家具付き物件の室内写真"></div><span>家具家電付き<br>物件ガイド</span></li>
    </ul>
  </div>
</section>

<section class="news">
  <div class="wrap">
    <div class="news-col">
      <h2>TOPICS</h2>
      <ul>
        <li>学生会館特集「一人暮らし準備の基本」を公開しました</li>
        <li>新年度の学生会館 空室状況を更新しました</li>
        <li>学生会館 VS アパート比較ページをリニューアル</li>
        <li>女子学生専用マンションの特集を追加しました</li>
        <li>寮・学生会館レポートに新しい記事を追加</li>
        <li>入居までの流れページを更新しました</li>
        <li>学生会館Q&amp;Aに新しい質問を追加しました</li>
        <li>関西エリアの学生会館情報を追加しました</li>
        <li>サイトをリニューアルしました</li>
      </ul>
    </div>
    <div class="news-col">
      <h2>オススメ情報</h2>
      <ul>
        <li>学生マンション特集（首都圏・関西）</li>
        <li>学生会館を選ぶ前に読むポイント</li>
        <li>家賃の目安と初期費用のまとめ</li>
        <li>学生会館の一日（食事付きプラン）</li>
        <li>新生活の持ち物チェックリスト</li>
      </ul>
    </div>
    <div class="page-top"><svg width="14" height="10" viewBox="0 0 14 10"><path d="M1 8l6-6 6 6" stroke="#fff" stroke-width="2" fill="none"/></svg></div>
  </div>
</section>

<footer class="site-footer">
  <nav><a>運営会社</a>|<a>プライバシーポリシー</a>|<a>サイトマップ</a>|<a>お問い合わせ</a></nav>
  <p>© キャンパス寮ナビ All rights reserved.</p>
</footer>

</body>
</html>
```